Business Card Design Project

I am a property development company requiring a professional looking business card.
The name of the my company is KLV SUMMITRA. I have attached a couple of designs that I have created on my own, that can give you an idea of what I am after.
Above the wording KLV SUMMITRA, I have a orange arc above these words to signify the sun is begining to rise above the horizon.
I have a few designs; Middle Rays, Side Rays, Horizontals Rays which are OK, but I am looking for the better design.
The Rear design of the card is what I had came up with. If you have a better design, I am happy to see it.
The design of the card can follow what I have came up with, or it can be totally different. The fonts needs to be adjusted to another font that is more suitable.
The colours that I have used is what I think I would like to stick with. As I have mentioned, the orange arc is to signify the sun rising. If you have a better colour scheme, I would consider it.
Looking at dealing with first home buyers and proffesional people.
Business

```html
<!DOCTYPE html>
<html lang="en">
<head>
<meta charset="utf-8">
<title>KLV Summitra – Business Card</title>
<link rel="stylesheet" href="https://fonts.googleapis.com/css2?family=Didact+Gothic&display=swap">
<style>
  :root {
    --backdrop: #e7e3dd;
    --card: #050505;
    --ink: #ffffff;
    --sun: #f7922c;
    --shadow: rgba(0, 0, 0, 0.28);
  }
  * { margin: 0; padding: 0; box-sizing: border-box; }
  html, body {
    width: 1200px;
    height: 846px;
    overflow: hidden;
    background: var(--backdrop);
    font-family: "Didact Gothic", "Century Gothic", sans-serif;
    color: var(--ink);
  }
  .card {
    position: absolute;
    left: 341px;
    width: 581px;
    height: 322px;
    background: var(--card);
    overflow: hidden;
    box-shadow: 0 3px 8px var(--shadow);
  }
  .card--front { top: 43px; }
  .card--back  { top: 384px; }

  /* Front */
  .brand-dot {
    position: absolute;
    left: 239px;
    top: 24px;
    width: 102px;
    height: 102px;
    border-radius: 50%;
    background: var(--sun);
  }
  .brand-name {
    position: absolute;
    top: 131px;
    width: 100%;
    text-align: center;
    font-size: 40px;
    line-height: 40px;
    letter-spacing: 0.5px;
  }
  .brand-tagline {
    position: absolute;
    top: 176px;
    width: 100%;
    text-align: center;
    font-size: 12px;
    letter-spacing: 4.2px;
  }
  .holder {
    position: absolute;
    top: 222px;
    width: 100%;
    text-align: center;
    font-size: 19px;
  }
  .holder em { font-style: italic; }

  /* Back */
  .contact {
    position: absolute;
    left: 192px;
    top: 112px;
    width: 220px;
    text-align: center;
    font-size: 17px;
    line-height: 21px;
  }
  .contact em { font-style: italic; }
  .contact__rule {
    width: 220px;
    height: 1px;
    background: var(--ink);
    margin: 10px 0 11px;
  }
  .sun-accent {
    position: absolute;
    left: 449px;
    top: 78px;
    width: 220px;
    height: 220px;
    border-radius: 50%;
    background: var(--sun);
  }
</style>
</head>
<body>
  <section class="card card--front">
    <div class="brand-dot"></div>
    <h1 class="brand-name">KLV SUMMITRA</h1>
    <p class="brand-tagline">PROPERTY DEVELOPMENTS</p>
    <p class="holder">Marcus Lee - <em>Director</em></p>
  </section>

  <section class="card card--back">
    <address class="contact">
      <p>27 Harbour Lane Kirrawee</p>
      <p>NSW 2232 <em>Australia</em></p>
      <div class="contact__rule"></div>
      <p>0491570156</p>
      <p>marcus@klvsummitra.com.au</p>
      <p>www.klvsummitra.com.au</p>
    </address>
    <div class="sun-accent"></div>
  </section>
</body>
</html>
```